General pharmacy flyer for a pharmacy. see attached files for similar flyer design
picture should be of a black person/pharmacist
Services available
Repeat Prescription collection
Emergency Contraception
Contraceptive pill
Vitamins
and more.....
Pharmacy

```html
<!DOCTYPE html>
<html lang="en">
<head>
<meta charset="utf-8">
<title>Crest Pharmacy Flyer</title>
<link href="https://fonts.googleapis.com/css2?family=Orbitron:wght@800;900&family=Open+Sans:wght@400;700&display=swap" rel="stylesheet">
<style>
  :root {
    --page-bg: #ece8e2;
    --brand-blue: #0b62b4;
    --deep-blue: #0a5aa8;
    --sky-blue: #12a0e4;
    --light-cyan: #8fd6f5;
    --brand-green: #4fae3c;
    --green-light: #5dbb3f;
    --white: #ffffff;
    --photo-top: #cfe6f2;
    --photo-bottom: #9cc8e4;
  }
  html, body {
    margin: 0;
    padding: 0;
    width: 1200px;
    height: 1200px;
    overflow: hidden;
    background: var(--page-bg);
  }
  .canvas {
    position: relative;
    width: 1200px;
    height: 1200px;
  }
  .flyer {
    position: absolute;
    left: 204px;
    top: 40px;
    width: 906px;
    height: 1282px;
    transform: scale(0.8736);
    transform-origin: top left;
    background: var(--white);
    overflow: hidden;
    box-shadow: 0 6px 18px rgba(0,0,0,0.25);
  }
  .flyer-shapes {
    position: absolute;
    inset: 0;
  }
  .brand {
    position: absolute;
    left: 52px;
    top: 660px;
    display: flex;
    align-items: center;
    gap: 22px;
  }
  .brand-dot {
    width: 118px;
    height: 118px;
    border-radius: 50%;
    border: 9px solid var(--brand-blue);
    box-sizing: border-box;
  }
  .brand-name {
    font-family: "Orbitron", sans-serif;
    font-weight: 900;
    font-size: 36px;
    color: var(--brand-blue);
    letter-spacing: 0.5px;
  }
  .tagline {
    position: absolute;
    left: 50px;
    top: 840px;
    margin: 0;
    font-family: "Orbitron", sans-serif;
    font-weight: 800;
    font-size: 18px;
    line-height: 28px;
    color: var(--white);
  }
  .phone-box {
    position: absolute;
    left: 480px;
    top: 800px;
    width: 375px;
    height: 115px;
    border-radius: 0 0 20px 20px;
    background: linear-gradient(180deg, var(--green-light), var(--brand-green));
    display: flex;
    align-items: center;
    padding-left: 36px;
    box-sizing: border-box;
    gap: 18px;
  }
  .phone-number {
    font-family: "Orbitron", sans-serif;
    font-weight: 900;
    font-size: 36px;
    color: var(--white);
    letter-spacing: 1px;
  }
  .services {
    position: absolute;
    left: 50px;
    top: 966px;
    width: 820px;
    font-family: "Open Sans", sans-serif;
    font-size: 17px;
    line-height: 21px;
    color: var(--white);
  }
  .services-title {
    margin: 0;
    font-weight: 700;
    font-size: 17px;
  }
  .services-columns {
    display: flex;
  }
  .services-list {
    margin: 0;
    padding: 0;
    list-style: none;
  }
  .services-list.first { width: 429px; }
  .footer {
    position: absolute;
    left: 0;
    bottom: 0;
    width: 906px;
    height: 77px;
    background: var(--brand-green);
    font-family: "Open Sans", sans-serif;
    font-size: 17px;
    line-height: 25px;
    color: var(--white);
    text-align: center;
    padding-top: 12px;
    box-sizing: border-box;
  }
  .footer strong { font-weight: 700; }
</style>
</head>
<body>
<div class="canvas">
  <div class="flyer">
    <svg class="flyer-shapes" width="906" height="1282" viewBox="0 0 906 1282">
      <defs>
        <linearGradient id="photoTone" x1="0" y1="0" x2="0" y2="1">
          <stop offset="0" stop-color="var(--photo-top)"/>
          <stop offset="1" stop-color="var(--photo-bottom)"/>
        </linearGradient>
        <linearGradient id="panelTone" x1="0" y1="0" x2="1" y2="1">
          <stop offset="0" stop-color="var(--deep-blue)"/>
          <stop offset="0.45" stop-color="var(--sky-blue)"/>
          <stop offset="1" stop-color="var(--deep-blue)"/>
        </linearGradient>
        <linearGradient id="cyanEdge" x1="0" y1="0" x2="1" y2="0">
          <stop offset="0" stop-color="var(--white)"/>
          <stop offset="1" stop-color="var(--light-cyan)"/>
        </linearGradient>
      </defs>
      <path role="img" aria-label="Photo of a smiling team of pharmacists and medical staff in white coats and scrubs, led by a Black pharmacist holding a blue folder" d="M0,0 H906 V645 C600,640 250,560 0,430 Z" fill="url(#photoTone)"/>
      <path d="M0,430 C250,560 600,640 906,645 V662 C600,662 250,605 0,478 Z" fill="var(--brand-blue)"/>
      <path d="M0,792 C300,805 600,795 906,762 V780 C600,805 300,810 0,800 Z" fill="url(#cyanEdge)"/>
      <path d="M0,795 C300,808 600,800 906,775 V1205 H0 Z" fill="url(#panelTone)"/>
    </svg>

    <div class="brand">
      <div class="brand-dot"></div>
      <span class="brand-name">CREST PHARMACY</span>
    </div>

    <p class="tagline">Come visit Crest Pharmacy for<br>all your prescription need<br>and more</p>

    <div class="phone-box">
      <svg width="48" height="48" viewBox="0 0 48 48" aria-hidden="true">
        <circle cx="24" cy="24" r="21" fill="none" stroke="var(--white)" stroke-width="3"/>
        <path d="M17 13 l4 -1 l3 7 l-3 2 q2 5 6 7 l2 -3 l7 3 l-1 4 q-2 3 -6 2 q-9 -3 -13 -13 q-1 -5 1 -8 z" fill="var(--white)"/>
      </svg>
      <span class="phone-number">555 0142</span>
    </div>

    <section class="services">
      <h2 class="services-title">Our Services</h2>
      <div class="services-columns">
        <ol class="services-list first">
          <li>1.&nbsp; Free blood pressure check</li>
          <li>2.&nbsp; Free blood sugar screenings</li>
          <li>3.&nbsp; Free weight checks</li>
          <li>4.&nbsp; Money transfer</li>
          <li>5.&nbsp; Ask about our $10 generic prescription plan</li>
          <li>6.&nbsp; Free multivitamins</li>
          <li>7.&nbsp; Patient education/ Drug counselling</li>
          <li>8.&nbsp; ATM</li>
          <li>9.&nbsp; Transit cards</li>
        </ol>
        <ol class="services-list">
          <li>10. Senior citizen 10% off</li>
          <li>11. Free parking in gas station</li>
          <li>12. Free pick up &amp; delivery</li>
          <li>13. Fax</li>
          <li>14. 5c copy</li>
          <li>15. Accept ERX</li>
          <li>16. Knowledgeable pharmacist and staff</li>
          <li>17. And more.</li>
        </ol>
      </div>
    </section>

    <footer class="footer">
      12 Palm Street (Corner of Palm and Harbour Street) | Bay Quarter, Eastport, St Marlo<br>
      Tel <strong>555 0142</strong> | Email <strong>crestpharmacy@example.com</strong>
    </footer>
  </div>
</div>
</body>
</html>
```